Take Away Box Packaging

Reef Captain Dunmore - Fish & Chips is a popular fish and chip store located on Sydney’s beautiful northern beaches. It sits just across from the sandy shores of Dunmore Beach.
We would like to redesign our packaging to include the new logo (attached) we have had created, and key messages about our food. We are trying to keep our collateral clean and fresh focusing on the food.
We need 3 sizes for the packaging:
1. Burger box
2. Snack box
3. Family box
All specifications are attached.
Key messages to include on the box include:
> Reef Captain Dunmore has been creating delicious, mouth-watering fish and chips since 1993.
> Wild caught sustainable fish
> Cooked in 100% rice bran oil
Follow us on Friendbook: /ReefCaptainDunmoreFishChips
Ph: 9846 2157

```html
<!DOCTYPE html>
<html lang="en">
<head>
<meta charset="utf-8">
<title>Reef Captain Dunmore – Burger Box Dieline</title>
<link href="https://fonts.googleapis.com/css2?family=Fira+Sans+Condensed:ital,wght@0,400;0,500;0,600;1,400;1,500&display=swap" rel="stylesheet">
<style>
  :root{
    --orange:#e85c22;
    --navy:#1f3566;
    --cut:#3aa7e0;
    --paper:#ffffff;
    --backdrop:#f3f4f6;
    --ink:#2a2a2a;
    --photo-warm:#e9b640;
    --photo-deep:#7a4a22;
  }
  *{box-sizing:border-box;margin:0;padding:0}
  html,body{width:1200px;height:1000px;overflow:hidden}
  body{background:var(--backdrop);font-family:"Fira Sans Condensed",Arial,sans-serif;color:var(--ink)}
  .dieline{position:relative;width:1200px;height:1000px}
  .dieline svg.cutlines{position:absolute;inset:0}
  .panel{position:absolute;overflow:hidden}

  /* brand name stand-in */
  .brand{display:flex;align-items:center;gap:8px;color:var(--navy);font-weight:500;line-height:1}
  .brand-dot{width:12px;height:12px;border-radius:50%;background:var(--orange);flex:none}

  /* lid side: phone */
  .panel-phone{left:400px;top:90px;width:400px;height:180px}
  .phone-block{position:absolute;left:0;top:0;width:250px;height:180px;background:var(--orange);color:#fff;
    display:flex;align-items:center;justify-content:center;font-size:54px;letter-spacing:1px}
  .phone-band{position:absolute;left:250px;top:0;width:28px;height:180px;background:var(--navy);
    color:#fff;font-style:italic;font-size:13px;writing-mode:vertical-rl;display:flex;align-items:center;justify-content:center}
  .panel-phone .brand{position:absolute;left:290px;top:70px;font-size:17px;width:105px;flex-wrap:wrap}

  /* left side: contents */
  .panel-contents{left:180px;top:270px;width:220px;height:360px}
  .contents-note{position:absolute;left:24px;top:28px;width:150px;font-style:italic;font-size:13px;line-height:1.35}
  .panel-contents .brand{position:absolute;left:24px;bottom:40px;font-size:22px}

  /* front: hero */
  .panel-front{left:400px;top:270px;width:400px;height:360px}
  .panel-front .brand{position:absolute;left:22px;top:20px;font-size:24px}
  .hero-photo{position:absolute;left:22px;top:64px;width:356px;height:210px;
    background:radial-gradient(circle at 35% 55%,var(--photo-deep) 0%,#b2692c 32%,var(--photo-warm) 70%,#f5d97a 100%)}
  .badge{position:absolute;right:14px;top:50px;width:118px;padding:8px 9px;background:var(--orange);color:#fff;
    font-style:italic;font-weight:500;font-size:13px;line-height:1.2;text-align:center}
  .tagline{position:absolute;left:0;right:0;bottom:0;height:76px;background:var(--navy);color:#fff;
    font-style:italic;font-size:15px;line-height:1.3;padding:14px 26px;text-align:right}

  /* right side: big brand */
  .panel-brand{left:800px;top:270px;width:220px;height:360px}
  .panel-brand .brand{position:absolute;left:22px;top:120px;font-size:30px;flex-wrap:wrap;width:180px}
  .brand-sub{position:absolute;left:22px;top:205px;color:var(--navy);font-size:14px;letter-spacing:2px}
  .corner{position:absolute;right:0;bottom:0;width:0;height:0;border-left:150px solid transparent;border-bottom:110px solid var(--orange)}

  /* back: info */
  .panel-back{left:400px;top:630px;width:400px;height:290px}
  .back-phone{position:absolute;left:0;top:0;width:190px;height:118px;background:var(--orange);color:#fff;padding:18px 18px}
  .back-phone .label{font-style:italic;font-size:14px}
  .back-phone .number{font-size:38px;margin-top:6px}
  .panel-back .brand{position:absolute;left:210px;top:24px;font-size:20px;width:180px;flex-wrap:wrap}
  .mandatory{position:absolute;left:210px;top:102px;font-style:italic;font-size:11px}
  .nutrition{position:absolute;left:20px;top:134px;width:170px;height:130px;border:1px solid #555;border-radius:10px;
    padding:8px 10px;font-size:11px}
  .follow{position:absolute;left:210px;top:196px;width:180px;display:flex;gap:8px;align-items:flex-start;color:var(--navy);font-weight:600;font-size:12px;line-height:1.35}
  .follow p{min-width:0}
  .follow-icon{width:18px;height:18px;background:var(--navy);flex:none;margin-top:2px}
</style>
</head>
<body>
<main class="dieline">
  <svg class="cutlines" width="1200" height="1000" viewBox="0 0 1200 1000" aria-hidden="true">
    <g fill="#fff" stroke="var(--cut)" stroke-width="1.2">
      <path d="M420 90 L440 40 Q445 28 460 28 L740 28 Q755 28 760 40 L780 90 Z"/>
      <path d="M400 270 L400 120 L340 150 L340 250 Z"/>
      <path d="M800 270 L800 120 L860 150 L860 250 Z"/>
      <path d="M400 630 L400 780 L340 760 L340 650 Z"/>
      <path d="M800 630 L800 780 L860 760 L860 650 Z"/>
      <path d="M180 290 L140 310 L140 590 L180 610 Z"/>
      <path d="M1020 290 L1060 310 L1060 590 L1020 610 Z"/>
      <rect x="400" y="90" width="400" height="180"/>
      <rect x="180" y="270" width="840" height="360"/>
      <rect x="400" y="630" width="400" height="290"/>
    </g>
    <g stroke="var(--cut)" stroke-width="1" stroke-dasharray="4 3" fill="none">
      <line x1="420" y1="90" x2="780" y2="90"/>
      <line x1="400" y1="270" x2="800" y2="270"/>
      <line x1="400" y1="630" x2="800" y2="630"/>
      <line x1="400" y1="270" x2="400" y2="630"/>
      <line x1="800" y1="270" x2="800" y2="630"/>
      <line x1="180" y1="290" x2="180" y2="610"/>
      <line x1="1020" y1="290" x2="1020" y2="610"/>
    </g>
  </svg>

  <section class="panel panel-phone">
    <div class="phone-block">9846 2157</div>
    <div class="phone-band">Hungerline Phone Number:</div>
    <div class="brand"><span class="brand-dot"></span>Reef Captain Dunmore</div>
  </section>

  <section class="panel panel-contents">
    <p class="contents-note">This box contains:<br>Total Content &amp; Ingredients will be come here.</p>
    <div class="brand"><span class="brand-dot"></span>Reef Captain Dunmore</div>
  </section>

  <section class="panel panel-front">
    <div class="brand"><span class="brand-dot"></span>Reef Captain Dunmore</div>
    <div class="hero-photo" role="img" aria-label="Photo of a fish burger with chips in a takeaway box"></div>
    <p class="badge">Wild caught sustainable fish Cooked in 100% rice bran oil</p>
    <p class="tagline">We has been creating delicious, mouth-watering fish and chips since 1993.</p>
  </section>

  <section class="panel panel-brand">
    <div class="brand"><span class="brand-dot"></span>Reef Captain Dunmore</div>
    <p class="brand-sub">FISH AND CHIPS</p>
    <div class="corner"></div>
  </section>

  <section class="panel panel-back">
    <div class="back-phone">
      <p class="label">Hungerline Phone Number:</p>
      <p class="number">9846 2157</p>
    </div>
    <div class="brand"><span class="brand-dot"></span>Reef Captain Dunmore</div>
    <p class="mandatory">Other mandatory information here</p>
    <div class="nutrition">Nutritional Information</div>
    <div class="follow"><span class="follow-icon"></span><p>Follow us at Friendbook:<br>/ReefCaptainDunmoreFishChips</p></div>
  </section>
</main>
</body>
</html>
```